New Website for Belcourt Manor at www.belcourt.com.au

A new logo has been designed (through pixel forge) and we now want to align the look and feel of our website at www.belcourt.com.au to the new logo. The content and page names (e.g. Grounds) will remain largely unchanged for the new site, so please submit a new look "Home" page, using our new logo, current text and any photos you choose from the existing gallery at our website. I have also attached the current "Home" page photos.

Industry/Entity Type

Accommodation

Number of Pages Required

1 page

Requirements
Must have
• Logo to be presented on white background.

```html
<!DOCTYPE html>
<html lang="en">
<head>
<meta charset="utf-8">
<title>Belcourt Manor</title>
<link rel="stylesheet" href="https://fonts.googleapis.com/css2?family=Lato:wght@400;700;900&family=Caveat:wght@500&display=swap">
<style>
:root{
  --white:#ffffff;
  --ink:#2c3a4b;
  --muted:#8a94a0;
  --nav:#555b63;
  --blue:#0a7fc2;
  --sun:#f7d84a;
  --violet:#4e4499;
  --sky:#5fd6fb;
  --coral:#e46863;
  --night:#2a3545;
  --deep:#232a36;
  --rule:#eceef0;
}
*{margin:0;padding:0;box-sizing:border-box}
html,body{width:860px;height:1200px;overflow:hidden;background:var(--white)}
body{position:relative;font-family:'Lato',sans-serif;color:var(--ink)}
.abs{position:absolute}

/* header */
.site-header{position:absolute;left:0;top:0;width:860px;height:81px;border-bottom:1px solid var(--rule)}
.header-rule{position:absolute;left:0;top:58px;width:860px;height:1px;background:var(--rule)}
.brand{position:absolute;left:168px;top:14px;display:flex;align-items:center;gap:7px}
.brand-dot{width:18px;height:18px;border-radius:50%;background:var(--blue)}
.brand-name{font-family:'Lato',sans-serif;font-weight:700;font-size:19px;color:var(--blue);letter-spacing:.3px}
.address{position:absolute;right:168px;top:9px;text-align:right;font-family:'Caveat',cursive;color:var(--blue);line-height:11px}
.address .street{font-size:15px;line-height:15px}
.address .line{font-size:11px}
.main-nav{position:absolute;left:168px;top:65px;display:flex;gap:9.5px}
.main-nav a{font-size:6.6px;color:var(--nav);text-decoration:none;letter-spacing:.1px;position:relative;height:16px;display:block}
.main-nav a.active::after{content:"";position:absolute;left:0;right:0;top:14px;height:2px;background:var(--blue)}

/* hero */
.hero{position:absolute;left:0;top:81px;width:860px;height:403px;
  background:linear-gradient(180deg,#3e4a32 0%,#4d5a33 18%,#8a4a34 34%,#a8875a 50%,#9b8a5e 66%,#6b6352 82%,#58554d 100%)}
.hero-shade{position:absolute;inset:0;background:rgba(20,24,28,.25)}
.hero-title{position:absolute;left:0;width:860px;top:124px;text-align:center;font-weight:900;font-size:40px;letter-spacing:-.5px;color:var(--white)}
.hero-title .accent{color:var(--sun)}
.hero-sub{position:absolute;left:0;width:860px;top:174px;text-align:center;font-size:11px;color:var(--white);letter-spacing:.4px}
.hero-prev{position:absolute;left:22px;top:150px;width:23px;height:22px;background:var(--blue)}
.hero-next{position:absolute;left:815px;top:150px;width:23px;height:22px;border:1px solid rgba(255,255,255,.8)}
.hero-prev svg,.hero-next svg{position:absolute;left:7px;top:6px}
.scroll-cue{position:absolute;left:424px;top:382px}

/* intro */
.intro-photo{position:absolute;left:168px;top:529px;width:210px;height:161px;
  background:linear-gradient(160deg,#4e6a3a 0%,#7b8c4f 35%,#b98a5c 55%,#5fb0c4 70%,#3f5a30 100%)}
.intro-title{position:absolute;left:392px;top:526px;font-weight:700;font-size:14.2px;letter-spacing:1.6px;color:var(--ink)}
.intro-copy{position:absolute;left:392px;top:549px;width:300px;font-size:6.4px;line-height:10.8px;color:var(--muted);letter-spacing:.3px}
.intro-copy p{margin-bottom:10.6px}
.intro-copy a{color:var(--blue)}
.btn-outline{position:absolute;left:392px;top:673px;width:102px;height:18px;border:1.2px solid var(--ink);border-radius:2px;display:flex;align-items:center;justify-content:center;gap:14px;font-size:6.6px;letter-spacing:.8px;color:var(--ink)}

/* feature bands */
.features{position:absolute;left:0;top:734px;width:860px;height:161px;display:flex}
.feature{width:286.7px;height:161px;position:relative;color:var(--white)}
.feature.violet{background:var(--violet)}
.feature.sky{background:var(--sky)}
.feature.coral{background:var(--coral)}
.feature h3{position:absolute;left:36px;top:34px;font-size:7px;font-weight:700;letter-spacing:.8px}
.feature p{position:absolute;left:36px;top:47px;width:220px;font-size:6px;line-height:10.7px}
.feature .btn{position:absolute;left:36px;top:111px;width:76px;height:22px;border:1.2px solid var(--white);border-radius:2px;display:flex;align-items:center;justify-content:center;font-size:6.6px;font-weight:700}

/* testimonial */
.testimonial{position:absolute;left:0;top:895px;width:860px;height:267px;background:var(--night)}
.quote{position:absolute;left:160px;top:94px;width:540px;text-align:center;font-weight:700;font-size:11.4px;line-height:18px;color:var(--white);letter-spacing:-.2px}
.author{position:absolute;left:0;width:860px;top:163px;text-align:center;font-size:7px;color:var(--white)}
.dots{position:absolute;left:418px;top:241px;display:flex;gap:5px}
.dots span{width:4.5px;height:4.5px;border-radius:50%;background:var(--white)}
.dots span.on{background:var(--blue)}
.side-arrow{position:absolute;top:117px;width:22px;height:35px;background:var(--deep)}
.side-arrow svg{position:absolute;left:8px;top:14px}

/* footer */
.site-footer{position:absolute;left:0;top:1162px;width:860px;height:38px;background:var(--deep);font-size:6px;color:#c9ced6}
.copyright{position:absolute;left:168px;top:15px}
.copyright .name{color:var(--blue)}
.copyright .sep{color:#555d69;margin:0 4px}
.footer-nav{position:absolute;right:168px;top:15px;display:flex;gap:4px;font-size:5.3px;color:#8c95a2}
</style>
</head>
<body>

<header class="site-header">
  <div class="brand">
    <span class="brand-dot"></span>
    <span class="brand-name">Belcourt Manor</span>
  </div>
  <div class="address">
    <div class="street">42 Belcourt Lane</div>
    <div class="line">Ferndale, Gold Coast</div>
    <div class="line">Queensland, Australia</div>
  </div>
  <div class="header-rule"></div>
  <nav class="main-nav">
    <a class="active">MAIN</a><a>MANSION</a><a>BEDROOMS</a><a>OPTIONS</a><a>HARE AND HOUND</a><a>GROUNDS</a><a>LOCATION</a><a>GALLERY</a><a>CONTACT</a><a>AVAILABILITY</a><a>DIY WEDDINGS</a>
  </nav>
</header>

<section class="hero" role="img" aria-label="Aerial photo of the yellow manor with red tiled roofs, gravel driveway and surrounding trees">
  <div class="hero-shade"></div>
  <h1 class="hero-title"><span class="accent">BELCOURT</span> MANOR</h1>
  <div class="hero-sub">Belcourt Manor is a unique Gold Coast estate</div>
  <div class="hero-prev"><svg width="8" height="10" viewBox="0 0 8 10"><path d="M5 2 L2 5 L5 8" fill="none" stroke="#fff" stroke-width="1"/></svg></div>
  <div class="hero-next"><svg width="8" height="10" viewBox="0 0 8 10"><path d="M3 2 L6 5 L3 8" fill="none" stroke="#fff" stroke-width="1"/></svg></div>
  <svg class="scroll-cue" width="13" height="8" viewBox="0 0 13 8"><path d="M1 1 L6.5 7 L12 1" fill="none" stroke="#fff" stroke-width="1.2"/></svg>
</section>

<section class="intro">
  <div class="intro-photo" role="img" aria-label="Aerial photo of the manor with its resort pool and palm gardens"></div>
  <h2 class="intro-title">PALATIAL ESTATE AND LUXURY RESORT</h2>
  <div class="intro-copy">
    <p>On over 2 manicured garden acres, Belcourt Manor is a unique Gold Coast estate, centrally located in the prestigious rural suburb of Ferndale. <a>More about our Location</a></p>
    <p>The estate features a grand mansion, private pub (The Hare and Hound), sparkling resort pool, tennis court and playground.</p>
    <p>Magnificent properties rarely feel so warm and welcoming – so browse away and visit our <a>photo gallery</a> – and we look forward to having you stay as our guests.</p>
    <p>For prices, availability and guest reviews</p>
  </div>
  <div class="btn-outline"><span>VISIT STAYNEST</span><svg width="8" height="5" viewBox="0 0 8 5"><path d="M0 2.5 H7 M5 0.5 L7 2.5 L5 4.5" fill="none" stroke="#2c3a4b" stroke-width=".8"/></svg></div>
</section>

<section class="features">
  <div class="feature violet">
    <h3>GRAND MANSION</h3>
    <p>Lorem ipsum dolor sit amet, consectetur adipiscing elit. Duis ut lobortis nulla. Vestibulum ante ipsum primis in faucibus orci luctus et ultrices posuere cubilia Curae; Sed lacinia, est eget scelerisque blandit, nulla eros mollis erat, vel ornare quam sem ut nisi. Mauris eu dolor mi. Praesent fermentum nulla id nisi inter-dum faucibus.</p>
    <div class="btn">CLICK HERE</div>
  </div>
  <div class="feature sky">
    <h3>BEDROOMS</h3>
    <p>Lorem ipsum dolor sit amet, consectetur adipiscing elit. Duis ut lobortis nulla. Vestibulum ante ipsum primis in faucibus orci luctus et ultrices posuere cubilia Curae; Sed lacinia, est eget scelerisque blandit, nulla eros mollis erat, vel ornare quam sem ut nisi. Mauris eu dolor mi. Praesent fermentum nulla id nisi inter-dum faucibus.</p>
    <div class="btn">CLICK HERE</div>
  </div>
  <div class="feature coral">
    <h3>THE GROUNDS</h3>
    <p>Lorem ipsum dolor sit amet, consectetur adipiscing elit. Duis ut lobortis nulla. Vestibulum ante ipsum primis in faucibus orci luctus et ultrices posuere cubilia Curae; Sed lacinia, est eget scelerisque blandit, nulla eros mollis erat, vel ornare quam sem ut nisi. Mauris eu dolor mi. Praesent fermentum nulla id nisi inter-dum faucibus.</p>
    <div class="btn">CLICK HERE</div>
  </div>
</section>

<section class="testimonial">
  <div class="side-arrow" style="left:0"><svg width="6" height="8" viewBox="0 0 6 8"><path d="M4 1 L1 4 L4 7" fill="none" stroke="#fff" stroke-width="1"/></svg></div>
  <div class="side-arrow" style="left:838px"><svg width="6" height="8" viewBox="0 0 6 8"><path d="M2 1 L5 4 L2 7" fill="none" stroke="#fff" stroke-width="1"/></svg></div>
  <blockquote class="quote">LOREM IPSUM DOLOR SIT AMET, CONSECTETUR ADIPISICING ELIT, SED DO EIUSMOD TEMPOR INCIDIDUNT UT LABORE ET DOLORE MAGNA ALIQUA. UT ENIM AD MINIM VENIAM, QCUPIDATAT NON PROIDENT, SUNT IN CULPA QUI OFFICIA DESERUNT MOLLIT ANIM ID EST LABORUM. SED UT</blockquote>
  <div class="author">JOHN DOE, USA</div>
  <div class="dots"><span></span><span class="on"></span><span></span></div>
</section>

<footer class="site-footer">
  <div class="copyright">Copyright 2016 <span class="name">Belcourt Manor</span><span class="sep">|</span>All Rights Reserved</div>
  <nav class="footer-nav"><span>MANSION</span><span>BEDROOMS</span><span>OPTIONS</span><span>HARE AND HOUND</span><span>GROUNDS</span><span>LOCATION</span><span>GALLERY</span><span>CONTACT</span><span>AVAILABILITY</span><span>DIY WEDDINGS</span></nav>
</footer>

</body>
</html>
```